Corporate Identity Project for Veteran Transition Company

I am launching a company, Pathora.net. My tagline is:

Helping Veterans find great careers. Helping companies tap extra-ordinary talent.

This is my immediate need:
1. Stationary design that will appeal to both veterans and hiring companies.
2. Matching business card.

Next:
Ideally, I would like to hire someone who can also help me put together power-point presentations, or at least a template, of the same look and feel.

Extra credit: I already have a logo. I like it but could be persuaded to go with something else. If the winning designer, and only the winning designer, comes up with a better logo, I will pay a for it but don't want that to be what this is about.

More about the company:

Pathora's purpose is to help transitioning veterans find great jobs while helping companies tap the leadership skills, adaptability, and ability to work as team that defines veterans.

We do this by first helping veterans asses their individual strengths, interests, and transferrable skills. Next we help them map these to private sector career paths and teach them how to market themselves. In addition, we work with companies to onboard their veterans by offering a "Open Horizon Kickoff Workshop" to help vets succeed in civilian job cultures.

Our goal is create a scalable web based solution for all of our services so that we can cost efficiently serve the thousands of returning vets who are both geographically dispersed.

From a design stand point, I'm looking for something that will be professional enough to show CEO's of major companies as they will be our initial sponsors. It needs to look professional. While I am hoping you can help me with design and color palette etc. I do not want my design to look like it wears combat boots. i.e, no camouflage colors or military symbols.
Updates

Reason: First time user error :)

As the designs are coming in, a couple preferences that I seem to be developing and want to pass on to save everyone time:

1.  I like squared biz card edges vs. rounded.  Don't worry if your submission has rounded, I can visualize everything else just fine.
2.  I prefer a colored back of the card vs. a blank or white backing.

Thanks

Please keep in mind that I need the design to be able to work on both a business card and ppt template.

Excellent submissions so far.  I've just gone through them all and am going to eliminate several that simply don't fit into the criteria I updated earlier:

1.  Squared edges only
2.  Tag line must be on the front of the business card.

I will write what I want on the back in a couple of minutes.  

Thank you,

Tomas

Target Market(s)

CEOs, Heads of Human Resources at Meridian 300 companies.

Industry/Entity Type

Leadership

Requirements
Must have
• Must be able to use in ppt presentations so the company's look and feel is consistent.

On the back I'd like a Venn diagram similar to my second attachment. A central belief is that great jobs are all about finding something you are passionate about, inherantly good at doing, brings values to others, while allowing you to work in culture in which you can thrive.

Biz card info:

1. Logo
2. Tomas Lindqvist
3. Founder (below or by my name)
4. Phone number
5. Email: tomas.lindqvist@pathora.net
Note: Let's leave web address off until i'm ready to re-lanch the site.
Nice to have
• I am new to "Pixel Forum" so bear with me in using their technology. I would prefer to have two-way feedback so I don't waste your time while improving the odds of getting this exactly right so please do not hesitate to reach out.
Should not have
• No use of red-white-and blue or military motifs. While I aplaud the many not-for-profits out there helping vets, that apeal to "giving vets something back," I'm trying to come at this from a business proposition angle:

Vets have some terrific skills that businesses can want. They are just missing each other in the translation in getting hired and the help djusting to the new culture. That's where we come in!

```html
<!DOCTYPE html>
<html lang="en">
<head>
<meta charset="utf-8">
<title>Pathora Stationery</title>
<link rel="stylesheet" href="https://fonts.googleapis.com/css2?family=Source+Sans+3:wght@400;600;700&family=Norican&display=swap">
<style>
  :root {
    --navy: #2e4276;
    --blue: #1f86c8;
    --ink: #6f7276;
    --paper: #f7f7f8;
    --backdrop: #e4e1e1;
    --white: #ffffff;
  }
  * { margin: 0; padding: 0; box-sizing: border-box; }
  html, body { width: 1200px; height: 1200px; overflow: hidden; }
  body {
    position: relative;
    background: var(--backdrop);
    font-family: "Source Sans 3", Arial, sans-serif;
  }

  /* Letterhead */
  .letterhead {
    position: absolute; left: 72px; top: 118px;
    width: 696px; height: 977px;
    background: var(--paper);
  }
  .letterhead .address {
    position: absolute; left: 51px; top: 69px;
    font-size: 13px; line-height: 17px; color: var(--navy);
  }
  .letterhead .address strong { font-weight: 700; }
  .contact-list { position: absolute; list-style: none; color: var(--navy); }
  .contact-list li { display: flex; align-items: center; }
  .contact-list svg { fill: var(--blue); flex: none; }
  .letterhead .contact-list { left: 281px; top: 69px; font-size: 13px; line-height: 17px; }
  .letterhead .contact-list svg { width: 10px; height: 10px; margin-right: 10px; }
  .wordmark {
    position: absolute; font-weight: 600; color: var(--navy);
    letter-spacing: 0.5px; line-height: 1;
  }
  .letterhead .wordmark { right: 48px; top: 64px; font-size: 44px; }

  .letter-body {
    position: absolute; left: 72px; top: 228px; width: 580px;
    font-size: 13.5px; line-height: 19px; color: var(--ink);
  }
  .letter-body .salutation { font-weight: 700; margin-bottom: 19px; }
  .letter-body p { margin-bottom: 18px; }

  .signature {
    position: absolute; left: 66px; top: 728px;
    font-family: "Norican", cursive; font-size: 38px; color: #3b3d42;
  }
  .signer-title {
    position: absolute; left: 71px; top: 778px;
    font-size: 16px; letter-spacing: 0.5px; color: var(--blue);
  }

  .tagline {
    position: absolute; left: 119px; top: 929px;
    font-size: 13px; letter-spacing: 2px; color: var(--navy); font-weight: 600;
  }
  .footer-band { position: absolute; left: 0; bottom: 0; display: block; }
  .web {
    position: absolute; color: var(--white); letter-spacing: 2.4px;
  }
  .letterhead .web { right: 48px; bottom: 15px; font-size: 13px; }

  /* Business card front */
  .card-front {
    position: absolute; left: 811px; top: 181px;
    width: 322px; height: 180px; background: var(--paper);
  }
  .card-front .name {
    position: absolute; left: 14px; top: 41px;
    font-size: 12.5px; font-weight: 700; color: var(--navy);
  }
  .card-front .role {
    position: absolute; left: 14px; top: 57px;
    font-size: 8.5px; color: var(--blue); letter-spacing: 0.3px;
  }
  .card-front .wordmark { right: 12px; top: 40px; font-size: 37px; }
  .card-front .contact-list { left: 15px; top: 120px; font-size: 9px; line-height: 11px; }
  .card-front .contact-list svg { width: 7px; height: 7px; margin-right: 8px; }
  .card-front .web { right: 30px; bottom: 8px; font-size: 10px; }

  /* Business card back */
  .card-back {
    position: absolute; left: 814px; top: 423px;
    width: 320px; height: 180px; background: var(--navy);
    display: flex; align-items: center; justify-content: center;
  }
  .card-back .wordmark { position: static; color: var(--white); font-size: 38px; margin-top: 14px; }
</style>
</head>
<body>

<article class="letterhead">
  <div class="address"><strong>Pathora,</strong> 2480 Alder Crest Ave.<br>Suite 310, Linwood, CA 90417</div>
  <ul class="contact-list">
    <li><svg viewBox="0 0 10 10"><path d="M2 0h2l1 3-1.5 1a6 6 0 0 0 2.5 2.5L7 5l3 1v2a2 2 0 0 1-2 2A8 8 0 0 1 0 2a2 2 0 0 1 2-2z"/></svg>877-52-6190</li>
    <li><svg viewBox="0 0 10 10"><path d="M0 2h10v7H0z M1 3l4 3 4-3" fill="none" stroke="#1f86c8" stroke-width="1.4"/></svg>tomas.lindqvist@pathora.net</li>
  </ul>
  <div class="wordmark">Pathora</div>

  <section class="letter-body">
    <p class="salutation">Lorem Ipsum,</p>
    <p>Cras mattis consectetur purus sit amet fermentum. Etiam porta sem malesuada magna mollis euismod. Integer posuere erat a ante venenatis dapibus posuere velit aliquet. Cras justo odio, dapibus ac facilisis in, egestas eget quam. Aenean eu leo quam. Pellentesque ornare sem lacinia quam venenatis vestibulum.</p>
    <p>Vivamus sagittis lacus vel augue laoreet rutrum faucibus dolor auctor. Donec sed odio dui. Etiam porta sem malesuada magna mollis euismod. Morbi leo risus, porta ac consectetur ac, vestibulum at eros. Nullam id dolor id nibh ultricies vehicula ut id elit.</p>
    <p>Donec id elit non mi porta gravida at eget metus. Fusce dapibus, tellus ac cursus commodo, tortor mauris condimentum nibh, ut fermentum massa justo sit amet risus. Cras justo odio, dapibus ac facilisis in, egestas eget quam. Cum sociis natoque penatibus et magnis dis parturient montes, nascetur ridiculus mus.</p>
    <p>Cum sociis natoque penatibus et magnis dis parturient montes, nascetur ridiculus mus. Curabitur blandit tempus porttitor. Aenean lacinia bibendum nulla sed consectetur. Lorem ipsum dolor sit amet, consectetur adipiscing elit.</p>
    <p>Cras justo odio, dapibus ac facilisis in, egestas eget quam. Morbi leo risus, porta ac consectetur ac, vestibulum at eros. Duis mollis, est non commodo luctus, nisi erat porttitor ligula, eget lacinia odio sem nec elit. Integer posuere erat a ante venenatis dapibus posuere velit aliquet. Vivamus sagittis lacus vel augue laoreet rutrum faucibus dolor auctor.</p>
  </section>

  <div class="signature">Tomas Lindqvist</div>
  <div class="signer-title">FOUNDER</div>

  <div class="tagline">Open Horizon Kickoff Workshop</div>
  <svg class="footer-band" width="696" height="37" viewBox="0 0 696 37">
    <path d="M0 10H462L470 5V13H0z" fill="#1f86c8"/>
    <path d="M0 13H466L476 0H696V37H0z" fill="#2e4276"/>
  </svg>
  <div class="web">www.pathora.net</div>
</article>

<article class="card-front">
  <div class="name">Tomas Lindqvist</div>
  <div class="role">FOUNDER</div>
  <div class="wordmark">Pathora</div>
  <ul class="contact-list">
    <li><svg viewBox="0 0 10 10"><path d="M2 0h2l1 3-1.5 1a6 6 0 0 0 2.5 2.5L7 5l3 1v2a2 2 0 0 1-2 2A8 8 0 0 1 0 2a2 2 0 0 1 2-2z"/></svg>877-52-6190</li>
    <li><svg viewBox="0 0 10 10"><path d="M0 2h10v7H0z M1 3l4 3 4-3" fill="none" stroke="#1f86c8" stroke-width="1.4"/></svg>tomas.lindqvist@pathora.net</li>
  </ul>
  <svg class="footer-band" width="322" height="26" viewBox="0 0 322 26">
    <path d="M0 4H160L166 2V7H0z" fill="#1f86c8"/>
    <path d="M0 7H164L170 0H322V26H0z" fill="#2e4276"/>
  </svg>
  <div class="web">www.pathora.net</div>
</article>

<article class="card-back">
  <div class="wordmark">Pathora</div>
</article>

</body>
</html>
```